Logo needed for business card

Velistra Pty Ltd is in the business of healthcare and ecommerce.

We own and manage pharmacies and online health ecomerce sites.

We provide ecommerce consultants for companies looking for an ecommerce business startegy.

Think of it as the umbrella under which several healthcare brands may sit.

When I think of Velistra, I visulaise slick black/metalic colours, so please stay away from the common blue and green colours that seem to be so popular in this field.

Target Market(s)

CEOs and COOs

Industry/Entity Type

Healthcare

Contact Information for Business Card

Delphine Okoro
Director
Velistra Pty Ltd
4/237 Kelburn Pde
Ferncliff, WA 6917

Requirements
Must have
• Design must have scope to be implemented on the company's website and letterheads etc.

```html
<!DOCTYPE html>
<html lang="en">
<head>
<meta charset="utf-8">
<title>Velistra Business Card</title>
<link href="https://fonts.googleapis.com/css2?family=Open+Sans:wght@400;600;700&display=swap" rel="stylesheet">
<style>
  :root {
    --graphite: #464b53;
    --graphite-dark: #3c4047;
    --signal-red: #c8362a;
    --paper: #f4f4f4;
    --paper-shade: #e6e6e6;
    --ink: #3a3e45;
    --stage: #d9dadc;
    --white: #ffffff;
  }
  * { margin: 0; padding: 0; box-sizing: border-box; }
  html, body {
    width: 1200px;
    height: 900px;
    overflow: hidden;
    background: var(--stage);
    font-family: "Open Sans", sans-serif;
  }
  .card {
    position: absolute;
    width: 600px;
    height: 366px;
    overflow: hidden;
    box-shadow: 0 10px 28px rgba(0, 0, 0, 0.25);
  }

  /* Back of card */
  .card--back {
    left: 300px;
    top: 52px;
    background: linear-gradient(160deg, var(--graphite), var(--graphite-dark));
  }
  .card--back .accent-bar {
    position: absolute;
    left: 0;
    top: 112px;
    width: 270px;
    height: 18px;
    background: var(--signal-red);
  }
  .card--back .brand {
    position: absolute;
    right: 36px;
    top: 36px;
  }

  /* Brand lockup */
  .brand {
    display: flex;
    align-items: center;
    gap: 12px;
  }
  .brand-name {
    font-weight: 700;
    font-size: 30px;
    color: var(--white);
    letter-spacing: 0.5px;
  }
  .brand-dot {
    width: 30px;
    height: 30px;
    border-radius: 50%;
    border: 4px solid var(--white);
  }

  /* Front of card */
  .card--front {
    left: 300px;
    top: 478px;
    background: linear-gradient(180deg, var(--paper), var(--paper-shade));
  }
  .card--front .faint-circle {
    position: absolute;
    left: 40px;
    top: 40px;
    width: 300px;
    height: 300px;
    border-radius: 50%;
    border: 26px solid rgba(0, 0, 0, 0.045);
  }
  .header-band {
    position: absolute;
    left: 0;
    top: 28px;
    width: 100%;
    height: 100px;
    background: var(--graphite);
  }
  .header-band .brand {
    position: absolute;
    left: 34px;
    top: 30px;
  }
  .header-band .accent-bar {
    position: absolute;
    left: 372px;
    right: 0;
    top: 52px;
    height: 20px;
    background: var(--signal-red);
  }
  .company {
    position: absolute;
    left: 36px;
    top: 226px;
    font-size: 15px;
    line-height: 20px;
    font-style: normal;
    color: var(--ink);
  }
  .company-name { font-weight: 700; }
  .person {
    position: absolute;
    left: 372px;
    top: 178px;
  }
  .person-name {
    font-size: 25px;
    color: var(--ink);
    line-height: 30px;
  }
  .person-role {
    font-size: 16px;
    font-weight: 600;
    color: var(--signal-red);
    letter-spacing: 0.8px;
  }
  .contact {
    position: absolute;
    left: 372px;
    top: 276px;
    font-size: 16px;
    line-height: 25px;
    color: var(--ink);
    list-style: none;
  }
  .contact-label {
    display: inline-block;
    width: 20px;
    font-weight: 700;
    font-style: italic;
    color: var(--signal-red);
  }
</style>
</head>
<body>
  <section class="card card--back" aria-label="Card back">
    <div class="accent-bar"></div>
    <div class="brand">
      <span class="brand-name">Velistra</span>
      <span class="brand-dot"></span>
    </div>
  </section>

  <section class="card card--front" aria-label="Card front">
    <div class="faint-circle"></div>
    <header class="header-band">
      <div class="brand">
        <span class="brand-name">Velistra</span>
        <span class="brand-dot"></span>
      </div>
      <div class="accent-bar"></div>
    </header>

    <address class="company">
      <div class="company-name">Velistra Pty Ltd</div>
      <div>4/237 Kelburn Pde Ferncliff</div>
      <div>WA 6917</div>
    </address>

    <div class="person">
      <div class="person-name">Delphine Okoro</div>
      <div class="person-role">DIRECTOR</div>
    </div>

    <ul class="contact">
      <li><span class="contact-label">t</span>(02) 9184 6207</li>
      <li><span class="contact-label">e</span>name@velistra.com</li>
    </ul>
  </section>
</body>
</html>
```